Harborline Talent IT Recruiting firm needs a business card design for Recruiters, Sourcers, and Account

We need business cards that allow us to change all contact info, names, titles (Recruiter, Sourcer, Account Manager, Director, CEO, etc) per person since we have three offices, in three cities, Phoenix, Austin, and Las Vegas. We do recruiting and contractors for IT positions (Developers, Architects, Software Engineers, Security Engineers, Help Desk, DBAs, PMs, Scrum Masters, etc.) Our client companies are very diverse from Crestline 250 to silicone Valley type start-ups.

So, while we what hip, techie, and quirky, it still needs to be professional. Primary color we use is blue, with silver as a secondary color.

Target Market(s)

IT, Technology

Industry/Entity Type

Business

Contact Information for Business Card

Company name: Harborline Talent, Inc.
Website: www.harborlinetalent-example.com
Logos for ProCircle, Quillo, and Roomwall

Name, Title, Office Number, Cell Number, email

Font styles to use
Serif
Sans Serif

Colors
0455a3
d5d5d5

Requirements
Nice to have
• The grey I selected below is not necessary - but, would like silver included. I included a card design (File 3: HTI early trial example.jpg) that I had started on. It's very rough, and not quite what we're looking for, but what we did like is the logo, big, maybe a bit faded, off center, goes out of frame, etc. Still looking for other ideas - you are the pros! But, just an idea of a design element we liked.

```html
<!DOCTYPE html>
<html lang="en">
<head>
<meta charset="utf-8">
<title>Harborline Talent — Business Card</title>
<link rel="stylesheet" href="https://fonts.googleapis.com/css2?family=Marcellus&family=Open+Sans:wght@400;600;700&display=swap">
<style>
  :root {
    --stage: #3a3a3c;
    --card-dark: #0d0e10;
    --card-light: #ffffff;
    --brand-blue: #0f8fdc;
    --brand-blue-deep: #0455a3;
    --ink: #111214;
    --silver: #d5d5d5;
    --white: #ffffff;
    --serif: "Marcellus", Georgia, serif;
    --sans: "Open Sans", Arial, sans-serif;
  }
  * { box-sizing: border-box; margin: 0; padding: 0; }
  html, body { width: 1200px; height: 852px; overflow: hidden; }
  body {
    background: var(--stage);
    position: relative;
    font-family: var(--sans);
  }
  .card {
    position: absolute;
    width: 525px;
    height: 300px;
    border-radius: 12px;
    overflow: hidden;
    top: 276px;
    box-shadow: 0 8px 22px rgba(0,0,0,.45);
  }
  .card--front { left: 50px; background: var(--card-dark); }
  .card--back  { left: 625px; background: var(--card-light); }

  .wordmark {
    display: flex;
    align-items: center;
    gap: 10px;
    font-family: var(--serif);
    letter-spacing: 1px;
    line-height: 1;
    white-space: nowrap;
  }
  .wordmark__dot {
    width: 30px; height: 30px;
    border-radius: 50%;
    background: var(--brand-blue);
    flex: none;
  }
  .card--front .wordmark {
    position: absolute;
    left: 0; right: 0; top: 112px;
    justify-content: center;
    font-size: 36px;
    color: var(--white);
  }
  .tagline {
    font-family: var(--serif);
    text-transform: uppercase;
    letter-spacing: 2px;
    white-space: nowrap;
  }
  .card--front .tagline {
    position: absolute;
    left: 0; right: 0; top: 180px;
    text-align: center;
    font-size: 14px;
    color: var(--white);
  }

  .card--back .wordmark {
    position: absolute;
    left: 26px; top: 50px;
    font-size: 26px;
    color: var(--ink);
  }
  .card--back .wordmark__dot { width: 26px; height: 26px; }
  .card--back .tagline {
    position: absolute;
    left: 28px; top: 96px;
    font-size: 11px;
    color: var(--ink);
  }
  .wave { position: absolute; inset: 0; }

  .person { position: absolute; left: 28px; top: 160px; }
  .person__name {
    font-weight: 700; font-size: 14px;
    color: var(--brand-blue); text-transform: uppercase;
  }
  .person__title { font-size: 11px; color: var(--brand-blue); margin-top: 2px; }
  .social { display: flex; gap: 6px; margin-top: 10px; }
  .social__item {
    font-size: 10px; font-weight: 600;
    color: var(--white); background: var(--brand-blue);
    padding: 3px 6px; border-radius: 3px;
  }

  .contact {
    position: absolute;
    right: 16px; top: 144px;
    list-style: none;
    color: var(--white);
    font-size: 10.5px;
    text-align: right;
    line-height: 1.6;
  }
  .contact li { display: flex; justify-content: flex-end; align-items: center; gap: 5px; white-space: nowrap; }
  .contact svg { width: 10px; height: 10px; fill: var(--white); flex: none; }
  .contact .no-icon { padding-right: 15px; }
</style>
</head>
<body>

<section class="card card--front" aria-label="Card front">
  <div class="wordmark"><span class="wordmark__dot"></span>HARBORLINE TALENT</div>
  <p class="tagline">Rising to the Challenge</p>
</section>

<section class="card card--back" aria-label="Card back">
  <svg class="wave" viewBox="0 0 525 300" preserveAspectRatio="none">
    <path d="M525 10 C430 30 370 60 320 110 C270 160 230 240 130 300 L525 300 Z" fill="var(--brand-blue)"/>
    <path d="M512 2 C417 24 357 54 306 104 C256 154 216 234 112 300 L122 300 C226 236 266 158 314 110 C364 62 424 34 525 8 Z" fill="var(--ink)"/>
    <path d="M0 266 C80 272 160 274 220 262 C180 282 100 286 0 280 Z" fill="var(--ink)"/>
    <path d="M0 286 C80 292 150 292 200 282 C160 298 90 300 0 300 Z" fill="var(--brand-blue)"/>
  </svg>

  <div class="wordmark"><span class="wordmark__dot"></span>HARBORLINE TALENT</div>
  <p class="tagline">Rising to the Challenge</p>

  <div class="person">
    <p class="person__name">Dana Whitford</p>
    <p class="person__title">CEO</p>
    <div class="social">
      <span class="social__item">Quillo</span>
      <span class="social__item">ProCircle</span>
      <span class="social__item">Roomwall</span>
    </div>
  </div>

  <ul class="contact">
    <li>602| 555-0143
      <svg viewBox="0 0 12 12"><path d="M2 1h3l1 3-2 1a7 7 0 0 0 3 3l1-2 3 1v3c-6 1-10-3-9-9z"/></svg></li>
    <li>602| 555-0178
      <svg viewBox="0 0 12 12"><rect x="3" y="1" width="6" height="3"/><rect x="1" y="5" width="10" height="4" rx="1"/><rect x="3" y="8" width="6" height="3"/></svg></li>
    <li>www.harborlinetalent-example.com
      <svg viewBox="0 0 12 12"><circle cx="6" cy="6" r="5" fill="none" stroke="#fff" stroke-width="1.2"/><path d="M1 6h10M6 1v10" stroke="#fff" stroke-width="1"/></svg></li>
    <li>dana@harborlinetalent-example.com
      <svg viewBox="0 0 12 12"><rect x="1" y="2.5" width="10" height="7" rx="1"/><path d="M1 3l5 4 5-4" fill="none" stroke="#0f8fdc" stroke-width="1"/></svg></li>
    <li>2710 W Cedar Ridge Rd, Suite 214
      <svg viewBox="0 0 12 12"><path d="M6 11C3 7 2 6 2 4.5a4 4 0 0 1 8 0C10 6 9 7 6 11z"/><circle cx="6" cy="4.5" r="1.4" fill="#0f8fdc"/></svg></li>
    <li class="no-icon">Phoenix, AZ 85099, USA</li>
  </ul>
</section>

</body>
</html>
```